Defense Attorney Business Card Design Project/ Stationary

I am looking for a distinctive business card design for my solo law practice.
I practice criminal defense, both juvenile and adult, including DUI. I am a very experienced attorney with prior military experience. The design should convey a traditional, old school flair, but not be too stodgy or uptight. Some color. My logo should appear.

Project Deadline Extended Reason: I misunderstood how this project works and I was not prepared with my logo when this project ran the first time. Added Thursday, November 13, 2014

Reason: I was sent overseas on military duty last year, which interrupted this project. Thank you for your participation... I hope we can get this done this week! Thank you, Des

Target Market(s)

Regular everyday people looking for strong, knowledgeable, authoritative representation while they are faced with criminal charges. Many have never been charged with a crime before. A reassuring air is therefore desired.

Industry/Entity Type

Business

Contact Information for Business Card

My information is:
Desmond R. Whitcombe, Attorney at Law
735 Linden Avenue Suite 300
Oakland, California 94618
Tel: (510) 555-0183
Fax: (510) 555-0162
email: deswhitcombelaw@mailbrook.net
web: www.deswhitcombelaw.net

Font styles to use
Serif
Sans Serif
Decorative

Colors
0255a3
ffffff

Requirements
Must have
• Sharp lines, bold elements. Conservative use of colors, such as deep blues, burgundy, grays for example.
• While my logo says "Des Whitcombe", it should be modified to show "Desmond R. Whitcombe".
Should not have
• Cliche imagery such as scales of justice, gavels, Tower of Varenholt, etc.

```html
<!DOCTYPE html>
<html lang="en">
<head>
<meta charset="utf-8">
<title>Des Whitcombe — Business Card</title>
<link rel="stylesheet" href="https://fonts.googleapis.com/css2?family=Marcellus&family=Marcellus+SC&display=swap">
<style>
  :root {
    --backdrop: #e7e5e1;
    --paper: #fbfaf7;
    --teal: #0f5a69;
    --teal-deep: #0b4d5b;
    --emboss: #dcdad4;
    --ink: #1a5666;
    --white: #ffffff;
  }
  * { margin: 0; padding: 0; box-sizing: border-box; }
  html, body {
    width: 1200px; height: 800px; overflow: hidden;
    background: var(--backdrop);
  }
  .canvas {
    width: 1200px; height: 800px;
    display: flex; align-items: center; justify-content: center;
  }
  .card {
    position: relative;
    width: 840px; height: 480px;
    background: var(--paper);
    box-shadow: 0 10px 30px rgba(0,0,0,0.12);
    overflow: hidden;
    font-family: "Marcellus", serif;
  }
  .brand {
    position: absolute; top: 150px; left: 0; right: 0;
    display: flex; align-items: center; justify-content: center; gap: 18px;
    color: var(--emboss);
  }
  .brand-mark {
    width: 46px; height: 46px; border-radius: 50%;
    background: var(--emboss);
  }
  .brand-name {
    font-family: "Marcellus", serif;
    font-size: 40px; letter-spacing: 1px; line-height: 1;
  }
  .rule {
    position: absolute; left: 0; right: 0; top: 262px;
    height: 3px; background: var(--teal);
  }
  .name-band {
    position: absolute; left: 0; right: 0; top: 272px; height: 68px;
    background: var(--teal);
    display: flex; align-items: center; padding-left: 150px;
    color: var(--white);
  }
  .name-band .name {
    font-family: "Marcellus SC", serif;
    font-size: 32px; letter-spacing: 1.5px;
  }
  .name-band .title {
    font-family: "Marcellus SC", serif;
    font-size: 22px; letter-spacing: 1.5px;
    margin-left: 16px; padding-left: 16px;
    border-left: 2px solid var(--white);
    line-height: 1.1;
  }
  .address-band {
    position: absolute; left: 0; right: 0; top: 410px; bottom: 0;
    background: var(--teal-deep);
  }
  .contact-area {
    position: absolute; left: 0; right: 0; top: 340px; height: 94px;
    background: var(--paper);
    border-bottom-right-radius: 56px;
  }
  .contact {
    position: absolute; top: 352px; left: 0; right: 0;
    display: grid; grid-template-columns: 440px 1fr; column-gap: 28px;
    color: var(--ink); font-size: 20px; line-height: 34px;
  }
  .contact .col-left { text-align: right; }
  .contact .tag { margin: 0 6px; }
  .address {
    position: absolute; left: 40px; bottom: 12px;
    color: var(--white);
    font-family: "Marcellus SC", serif;
    font-size: 22px; letter-spacing: 1px;
  }
</style>
</head>
<body>
<main class="canvas">
  <section class="card" aria-label="Attorney business card">
    <div class="brand">
      <span class="brand-mark" aria-hidden="true"></span>
      <span class="brand-name">Des Whitcombe</span>
    </div>

    <div class="rule"></div>
    <div class="name-band">
      <span class="name">Desmond R. Whitcombe</span>
      <span class="title">Attorney</span>
    </div>

    <div class="address-band"></div>
    <div class="contact-area"></div>
    <div class="contact">
      <div class="col-left">
        <div>(510) 555-0183<span class="tag">[T]</span></div>
        <div>deswhitcombelaw@mailbrook.net<span class="tag">[E]</span></div>
      </div>
      <div class="col-right">
        <div><span class="tag">[F]</span>(510) 555-0162</div>
        <div><span class="tag">[W]</span>www.deswhitcombelaw.net</div>
      </div>
    </div>

    <div class="address">735 Linden Avenue Suite 300 Oakland, California 94618</div>
  </section>
</main>
</body>
</html>
```